INNOVATION WEBSITE NEEDED: Agency from NZ needs YOU

Please see the enclosed documents for a detailed brief. It needs to be clean / simple / elegant / premium looking - that will appeal to companies that range from start-up to multi-national!
Note:
Perhaps instead of an actual shop, people can press an 'enquire now' button?

Target Market(s)

Start ups to multi-nationals

Industry/Entity Type

Marketing

Number of Pages Required

5+ page

Requirements
Must have
• Wordpress
• SEO
• Format friendly (mobile / tablet / etc)
• I have the URL: www.qu-tessaroly.com - I would like a working website. Please let me know what else you require to 'go live' with. Thanks!
Nice to have
• Please use / improve on my current ideas
• Perhaps use my logo icon (in different colours) for each 'product'?

```html
<!DOCTYPE html>
<html lang="en">
<head>
<meta charset="utf-8">
<title>Qu-Tessaroly — Delivering Big Ideas</title>
<link href="https://fonts.googleapis.com/css2?family=Roboto:wght@300;400;500;700&family=Roboto+Condensed:wght@300;400;700&display=swap" rel="stylesheet">
<style>
:root{
  --navy:#0c2a62;
  --blue:#4f8fd8;
  --sky:#5f9edc;
  --pale:#dbe9f8;
  --green:#6cb33f;
  --grey-bg:#f1f2f4;
  --grey-line:#cfd5dd;
  --text:#5b6574;
  --white:#ffffff;
}
*{box-sizing:border-box;margin:0;padding:0}
html,body{width:1200px;height:3852px;overflow:hidden}
body{font-family:"Roboto",Arial,sans-serif;color:var(--text);background:var(--white);font-size:13px;line-height:1.5}
h1,h2,h3,h4{font-family:"Roboto Condensed","Arial Narrow",sans-serif;color:var(--navy)}
.wrap{width:1040px;margin:0 auto;position:relative}
.btn{display:inline-block;font:500 12px "Roboto",sans-serif;padding:8px 16px;border-radius:3px;text-decoration:none}

/* header */
.site-header{height:116px;display:flex;flex-direction:column;align-items:center;justify-content:center}
.brand{display:flex;align-items:center;gap:10px}
.brand-mark{width:24px;height:24px;border-radius:50%;background:var(--navy)}
.brand-name{font:700 26px "Roboto Condensed",sans-serif;color:var(--navy);letter-spacing:1px}
.brand-tag{font-size:10px;letter-spacing:3px;color:var(--navy);margin-top:2px;text-transform:uppercase}
.main-nav{height:40px;background:var(--blue)}
.main-nav .wrap{display:flex;align-items:center;height:40px}
.main-nav a{color:var(--white);font:500 11px "Roboto",sans-serif;text-transform:uppercase;padding:0 22px;line-height:40px;text-decoration:none}
.main-nav a.active{background:var(--navy)}
.nav-social{margin-left:auto;display:flex;gap:6px}
.nav-social span{width:20px;height:20px;border:1.5px solid var(--white);border-radius:50%}

/* hero */
.hero{height:380px;position:relative;overflow:hidden}
.hero-photo{position:absolute;inset:0;background:linear-gradient(90deg,#5d4a2e 0%,#8c7a55 22%,#b9b29f 45%,#d8d6cf 70%,#e3e2dd 100%)}
.hero-copy{position:absolute;right:150px;top:96px;width:330px;text-align:center}
.hero-copy h1{font-size:30px;line-height:1.15;font-weight:700}
.hero-copy .btn{background:var(--navy);color:var(--white);margin-top:18px}
.hero-arrow{position:absolute;top:160px;color:var(--white);font-size:34px;opacity:.8}
.hero-wave{position:absolute;bottom:0;left:0}

/* products */
.products{height:560px;padding-top:40px}
.product-row{display:grid;grid-template-columns:repeat(4,1fr);gap:40px;padding:0 40px}
.product{text-align:center}
.product-icon{width:110px;height:110px;margin:0 auto 16px;border-radius:50%;background:var(--pale);border:6px solid #eef4fb;display:flex;align-items:center;justify-content:center}
.product-icon span{width:54px;height:54px;border-radius:50%;background:var(--blue)}
.product h3{font-size:18px;font-weight:700;margin-bottom:8px}
.product p{font-size:11px;color:var(--text);min-height:66px}
.product-foot{display:flex;justify-content:center;align-items:center;gap:14px;margin-top:10px}
.price{font:700 14px "Roboto",sans-serif;color:var(--navy)}
.btn-green{background:var(--green);color:var(--white);padding:6px 12px}
.slide-arrow{position:absolute;top:90px;font-size:30px;color:#a8b3c2}

/* reboot */
.reboot{height:430px;background:var(--grey-bg);padding-top:52px;text-align:center}
.section-title{display:flex;justify-content:center;align-items:center;gap:12px;font-size:26px;font-weight:400}
.section-title .dot{width:24px;height:24px;border-radius:50%;background:var(--navy)}
.reboot .lead{margin:18px 0 32px;font-size:13px}
.steps{position:relative;display:grid;grid-template-columns:repeat(4,1fr);width:860px;margin:0 auto}
.steps::before{content:"";position:absolute;top:18px;left:107px;right:107px;height:2px;background:var(--grey-line)}
.step{position:relative;display:flex;flex-direction:column;align-items:center}
.step-tick{width:38px;height:38px;border-radius:50%;background:#6d7480;display:flex;align-items:center;justify-content:center;border:4px solid var(--grey-bg)}
.step-tick.off{background:#b9bfc8}
.step p{font-size:10.5px;width:160px;margin-top:14px}
.reboot-actions{margin-top:36px;display:flex;justify-content:center;gap:14px}
.btn-navy{background:var(--navy);color:var(--white)}
.btn-grey{background:#c3c8cf;color:var(--white)}

/* how it works */
.how{height:420px;background:var(--sky);color:var(--white);text-align:center;padding-top:48px}
.how h2{color:var(--white);font-size:34px;font-weight:300;letter-spacing:1px}
.how .lead{width:560px;margin:12px auto 34px;font-size:13px}
.how-steps{display:flex;justify-content:center;align-items:center}
.how-step{width:240px}
.how-icon{width:100px;height:100px;border-radius:50%;background:var(--white);margin:0 auto}
.how-step p{font-size:10.5px;margin-top:20px;padding:0 18px}
.how-arrow{width:110px;margin-top:-70px}

/* what we do */
.about{height:365px;padding-top:50px}
.about-cols{display:grid;grid-template-columns:repeat(3,1fr);gap:60px;padding:0 40px}
.about-col{text-align:center}
.about-icon{width:52px;height:52px;border-radius:50%;background:var(--navy);margin:0 auto 12px}
.about-col h3{font-size:20px;font-weight:700}
.about-col h4{font:500 12px "Roboto",sans-serif;color:var(--navy);margin:6px 0 10px}
.about-col p{font-size:11px}
.btn-outline{border:1.5px solid var(--navy);color:var(--navy);margin-top:14px;padding:6px 14px;font-size:11px}

/* shop */
.shop{height:520px;background:var(--sky);padding-top:36px}
.shop .section-title{color:var(--white);justify-content:flex-start;font-size:22px;font-weight:700;padding-left:40px}
.shop .section-title .dot{background:var(--white)}
.shop-cards{display:grid;grid-template-columns:repeat(3,1fr);gap:34px;margin-top:22px;padding:0 40px}
.card{background:var(--white);text-align:center;height:366px}
.card-top{height:56px;display:flex;align-items:center;justify-content:center}
.card-top span{width:36px;height:36px;border-radius:50%;background:var(--navy)}
.card h3{background:var(--pale);font-size:21px;font-weight:700;padding:8px 0}
.card .price{display:block;font-size:24px;font-weight:300;color:var(--navy);margin:12px 0 10px}
.card p{font-size:11px;line-height:1.45;padding:0 34px;margin-bottom:8px}
.card .btn{background:#8fb4de;color:var(--white);margin-top:4px}
.dots{display:flex;justify-content:center;gap:8px;margin-top:18px}
.dots span{width:10px;height:10px;border-radius:50%;background:rgba(255,255,255,.5)}
.dots span.on{background:var(--white)}

/* chat */
.chat{height:790px;background:var(--navy);color:#c9d5ea;padding-top:60px}
.chat h2{color:var(--white);text-align:center;font-size:28px;font-weight:700}
.chat .lead{text-align:center;font-size:12px;width:900px;margin:12px auto 50px}
.chat-grid{display:grid;grid-template-columns:300px 1fr;gap:60px;padding:0 60px}
.info-item{display:flex;gap:14px;margin-bottom:24px;font-size:11.5px;color:var(--white)}
.info-item svg{flex:none}
.social-label{font:700 13px "Roboto",sans-serif;color:var(--white);margin:30px 0 10px}
.social-row{display:flex;gap:10px}
.social-row span{width:24px;height:24px;background:var(--white);border-radius:3px}
.contact-form h3{color:var(--white);text-align:center;font-size:20px;margin-bottom:20px}
.form-grid{display:grid;grid-template-columns:1fr 1fr;gap:18px 26px}
.field label{display:block;font-size:10px;color:var(--white);text-transform:uppercase;margin-bottom:4px}
.field .input{height:30px;background:var(--white)}
.field.full{grid-column:1/3}
.field.full .input{height:110px}
.form-submit{text-align:center;margin-top:22px}
.form-submit .btn{background:var(--blue);color:var(--white);padding:8px 30px}

/* footer */
.site-footer{height:231px;display:flex;flex-direction:column;align-items:center;justify-content:flex-start;padding-top:26px;gap:6px;font-size:10px;color:var(--text)}
.footer-nav{display:flex;gap:6px;text-transform:uppercase}
</style>
</head>
<body>

<header class="site-header">
  <div class="brand"><span class="brand-mark"></span><span class="brand-name">QU-TESSAROLY</span></div>
  <div class="brand-tag">Powering the future</div>
</header>

<nav class="main-nav">
  <div class="wrap">
    <a class="active">Home</a><a>Shop</a><a>Our Purpose</a><a>What We Do</a><a>The Team</a><a>Contact Us</a>
    <div class="nav-social"><span></span><span></span><span></span><span></span></div>
  </div>
</nav>

<section class="hero">
  <div class="hero-photo" role="img" aria-label="Photo of a glass jar filled with coins with a green seedling growing from it, on a wooden table"></div>
  <div class="hero-copy">
    <h1>QU-TESSAROLY:<br>DELIVERING BIG IDEAS,<br>FAST AND<br>AFFORDABLE</h1>
    <a class="btn">CONTACT</a>
  </div>
  <span class="hero-arrow" style="left:20px">&#8249;</span>
  <span class="hero-arrow" style="right:20px">&#8250;</span>
  <svg class="hero-wave" width="1200" height="40" viewBox="0 0 1200 40"><path d="M0 40 L0 22 Q300 0 600 18 T1200 8 L1200 40 Z" fill="#ffffff"/></svg>
</section>

<section class="products">
  <div class="wrap">
    <span class="slide-arrow" style="left:0">&#8249;</span>
    <span class="slide-arrow" style="right:0">&#8250;</span>
    <div class="product-row">
      <div class="product">
        <div class="product-icon"><span></span></div>
        <h3>THE SPARK</h3>
        <p>A fast, friendly half-day session to brew fresh ideas for your team and your business goals.</p>
        <div class="product-foot"><span class="price">$Free</span><a class="btn btn-green">Read More</a></div>
      </div>
      <div class="product">
        <div class="product-icon"><span></span></div>
        <h3>THE PATHFINDER</h3>
        <p>A focused one-day workshop that trains your people to spot and shape new ideas with confidence.</p>
        <div class="product-foot"><span class="price">$499</span><a class="btn btn-green">Read More</a></div>
      </div>
      <div class="product">
        <div class="product-icon"><span></span></div>
        <h3>THE NAVIGATOR</h3>
        <p>A quiet, sharp review of your process, with clear steps to move quicker and waste less effort.</p>
        <div class="product-foot"><span class="price">$749</span><a class="btn btn-green">Read More</a></div>
      </div>
      <div class="product">
        <div class="product-icon"><span></span></div>
        <h3>THE TRAILBLAZER</h3>
        <p>A bold program for leaders who want to break the mould and launch something truly new.</p>
        <div class="product-foot"><span class="price">$649</span><a class="btn btn-green">Read More</a></div>
      </div>
    </div>
  </div>
</section>

<section class="reboot">
  <h2 class="section-title"><span class="dot"></span><span>RE-BOOT OR <b>KICK-START…?</b></span></h2>
  <p class="lead">Do you need to reboot or kick start your company's innovation capabilities in terms of process, people or projects?</p>
  <div class="steps">
    <div class="step"><span class="step-tick"><svg width="16" height="12" viewBox="0 0 16 12"><path d="M1 6 L6 11 L15 1" stroke="#fff" stroke-width="2.5" fill="none"/></svg></span><p>If you have answered yes to any of the above, contact Qu-Tessaroly</p></div>
    <div class="step"><span class="step-tick"><svg width="16" height="12" viewBox="0 0 16 12"><path d="M1 6 L6 11 L15 1" stroke="#fff" stroke-width="2.5" fill="none"/></svg></span><p>If you have answered yes to any of the above, contact Qu-Tessaroly</p></div>
    <div class="step"><span class="step-tick off"><svg width="16" height="12" viewBox="0 0 16 12"><path d="M1 6 L6 11 L15 1" stroke="#fff" stroke-width="2.5" fill="none"/></svg></span><p>If you have answered yes to any of the above, contact Qu-Tessaroly</p></div>
    <div class="step"><span class="step-tick off"><svg width="16" height="12" viewBox="0 0 16 12"><path d="M1 6 L6 11 L15 1" stroke="#fff" stroke-width="2.5" fill="none"/></svg></span><p>If you have answered yes to any of the above, contact Qu-Tessaroly</p></div>
  </div>
  <div class="reboot-actions"><a class="btn btn-navy">Re-boot or Kick-start</a><a class="btn btn-grey">Read more info</a></div>
</section>

<section class="how">
  <h2>HOW IT WORKS</h2>
  <p class="lead">Instead of asking for a pure fixed fee with most agencies, we have a price list. You can order our services online.</p>
  <div class="how-steps">
    <div class="how-step"><div class="how-icon" role="img" aria-label="Icon of a shopping choice"></div><p>Choose a product from our list of services that best suits your needs, then order it online in a few clicks.</p></div>
    <svg class="how-arrow" width="110" height="40" viewBox="0 0 110 40"><path d="M5 30 Q55 -4 98 24" stroke="#fff" stroke-width="3" fill="none"/><path d="M88 26 L100 26 L96 14" stroke="#fff" stroke-width="3" fill="none"/></svg>
    <div class="how-step"><div class="how-icon" role="img" aria-label="Icon of a scheduled session"></div><p>Within one to two business days our team will contact you to plan the session and agree on the right time.</p></div>
    <svg class="how-arrow" width="110" height="40" viewBox="0 0 110 40"><path d="M5 30 Q55 -4 98 24" stroke="#fff" stroke-width="3" fill="none"/><path d="M88 26 L100 26 L96 14" stroke="#fff" stroke-width="3" fill="none"/></svg>
    <div class="how-step"><div class="how-icon" role="img" aria-label="Icon of delivered results"></div><p>If you need a tailored approach, simply give the team a call and we will shape a plan that fits.</p></div>
  </div>
</section>

<section class="about">
  <div class="wrap about-cols">
    <div class="about-col">
      <div class="about-icon" role="img" aria-label="Team icon"></div>
      <h3>WHAT WE DO</h3>
      <h4>We innovate. For you. The most common things we hear are</h4>
      <p>"I need a breakthrough innovation, but I'm having a hard time knowing where to start or who can help us get there."</p>
      <a class="btn btn-outline">READ MORE</a>
    </div>
    <div class="about-col">
      <div class="about-icon" role="img" aria-label="Purpose icon"></div>
      <h3>OUR PURPOSE</h3>
      <h4>Our purpose is to re-define how companies like yours get great innovation. Quickly.</h4>
      <p>The team at Qu-Tessaroly has worked with clients large and small and has seen what works and what slows things down.</p>
      <a class="btn btn-outline">READ MORE</a>
    </div>
    <div class="about-col">
      <div class="about-icon" role="img" aria-label="Brand icon"></div>
      <h3>QU-TESSAROLY</h3>
      <h4>Our purpose is to re-define how companies like yours get great innovation. Quickly.</h4>
      <p>The team at Qu-Tessaroly brings years of hands-on practice so your ideas reach the market faster and cheaper.</p>
      <a class="btn btn-outline">READ MORE</a>
    </div>
  </div>
</section>

<section class="shop">
  <div class="wrap">
    <h2 class="section-title"><span class="dot"></span><span>INNOVATION SHOP</span></h2>
    <div class="shop-cards">
      <div class="card">
        <div class="card-top"><span></span></div>
        <h3>THE TRAILBLAZER</h3>
        <span class="price">$649</span>
        <p>4 hours of dedicated support from the Qu-Tessaroly team.</p>
        <p>Use this for any idea that needs a fresh, honest outside view of a month.</p>
        <p>Your choice of a call, video or in-person session at your office.</p>
        <p>Great for leaders who want to move quickly and try things.</p>
        <a class="btn">Read More</a>
      </div>
      <div class="card">
        <div class="card-top"><span></span></div>
        <h3>THE ARCHITECT</h3>
        <span class="price">$1499</span>
        <p>2 days of "top-rate" support.</p>
        <p>Customisable to your specific needs. Could include:</p>
        <p>A working board to map out what needs to be done and any ideas you already have in place.</p>
        <p>Hands-on, action-oriented input that you can build on in the same day.</p>
        <a class="btn">Read More</a>
      </div>
      <div class="card">
        <div class="card-top"><span></span></div>
        <h3>GOLD CLASS</h3>
        <span class="price">$3499</span>
        <p>The workshop for serious growth.</p>
        <p>The full program covering objectives and structure of the session, input into your next projects and clear outcomes for senior teams.</p>
        <p>4 key themes to take forward.</p>
        <a class="btn">Read More</a>
      </div>
    </div>
    <div class="dots"><span class="on"></span><span></span><span></span></div>
  </div>
</section>

<section class="chat">
  <h2>LET'S HAVE A CHAT</h2>
  <p class="lead">The team at Qu-Tessaroly is flexible in terms of time and location – using today's technology we can be with you virtually anywhere, anytime. If you are in Europe, we can work while you sleep. Our aim is to be the most beautiful and creative innovation team in New Zealand. Give us a call – we're listening.</p>
  <div class="chat-grid">
    <div class="chat-info">
      <div class="info-item"><svg width="18" height="22" viewBox="0 0 18 22"><path d="M9 1 C4 1 1 5 1 9 C1 15 9 21 9 21 C9 21 17 15 17 9 C17 5 14 1 9 1 Z" fill="#fff"/><circle cx="9" cy="9" r="3" fill="#0c2a62"/></svg><span>24 Harbour Lane, Kelmscott Bay,<br>Auckland,<br>New Zealand</span></div>
      <div class="info-item"><svg width="20" height="14" viewBox="0 0 20 14"><rect x="0.5" y="0.5" width="19" height="13" fill="#fff"/><path d="M1 1 L10 8 L19 1" stroke="#0c2a62" stroke-width="1.5" fill="none"/></svg><span>Email:<br>hello@qu-tessaroly.com</span></div>
      <div class="info-item"><svg width="18" height="18" viewBox="0 0 18 18"><path d="M4 1 L7 5 L5 7 C6 10 8 12 11 13 L13 11 L17 14 L15 17 C8 17 1 10 1 3 Z" fill="#fff"/></svg><span>Telephone:<br>+64 21 555 0142</span></div>
      <div class="social-label">SOCIAL</div>
      <div class="social-row"><span></span><span></span><span></span><span></span><span></span><span></span></div>
    </div>
    <form class="contact-form">
      <h3>CONTACT NOW!</h3>
      <div class="form-grid">
        <div class="field"><label>Name</label><div class="input"></div></div>
        <div class="field"><label>Last</label><div class="input"></div></div>
        <div class="field"><label>E-mail</label><div class="input"></div></div>
        <div class="field"><label>Telephone</label><div class="input"></div></div>
        <div class="field full"><label>Message</label><div class="input"></div></div>
      </div>
      <div class="form-submit"><a class="btn">SUBMIT</a></div>
    </form>
  </div>
</section>

<footer class="site-footer">
  <div class="footer-nav"><span>Home</span>|<span>About Us</span>|<span>Our Services</span>|<span>Reviews</span>|<span>Contact Us</span></div>
  <div>© 2016 Qu-Tessaroly. All Rights Reserved — www.qu-tessaroly.com</div>
</footer>

</body>
</html>
```